"STYLE SNACKS" courses banner ads

Creation of 6 web banners for google display network and 1 image to be used on FaceBook.

Our website: http://www.qmvrk.org/
Our facebook: https://www.facebook.com/qmvrk/

The banners are meant to attract consumers to click and go to our landing page to find out more about our series of short courses training to be held in 4/5* hotels. The courses to be trained are Colour and Styling, Fabric Care and Leather Care.

Example of the short courses landing page: http://www.qmvrk.org/special-holiday-season-courses/

Target Market(s)

Females, 25-55 years old, interested in learning fashion styling, fabric care

Industry/Entity Type

Fashion

Font styles to use
Sans Serif

Colors
ec1f27
757575

Requirements
Must have
• Image used should have people and are happy/smiling.
• Some samples of pass banner ads images will be included: see the fabric care and open house samples
• Corporate colours are red, grey and black but addition of complementary colours will be great. Not necessary to use all the three corporate colours at the same time.
• Logos - to be provided (QmV.rk)
• TEXT:
• Style Snacks
• Short Courses held in hotels in June and July 2017
• Find out more!
Nice to have
• Asian person(s) in the image - please propose the stock image if necessary.
Should not have
• clip art
• fashion runway

```html
<!DOCTYPE html>
<html lang="en">
<head>
<meta charset="utf-8">
<title>Style Snacks – Banner Set</title>
<link rel="stylesheet" href="https://fonts.googleapis.com/css2?family=Montserrat:wght@800&family=Roboto:wght@400;500&family=Roboto+Condensed:wght@700&display=swap">
<style>
  :root {
    --stage: #1d1d1f;
    --red: #ec1f27;
    --red-deep: #b3060d;
    --red-dark: #8e0309;
    --white: #ffffff;
    --btn-top: #ffe34d;
    --btn-bottom: #f4a600;
    --btn-text: #2a1a00;
  }
  * { box-sizing: border-box; margin: 0; padding: 0; }
  html, body { width: 1200px; height: 1200px; overflow: hidden; }
  body { background: var(--stage); position: relative; font-family: "Roboto", Arial, sans-serif; }

  .banner {
    position: absolute;
    overflow: hidden;
    background: linear-gradient(135deg, var(--red) 0%, var(--red-deep) 70%, var(--red-dark) 100%);
    color: var(--white);
  }
  .banner svg.photo-layer { position: absolute; inset: 0; width: 100%; height: 100%; }

  .headline { position: absolute; font-family: "Montserrat", Arial, sans-serif; font-weight: 800; line-height: 1; text-align: center; text-transform: uppercase; white-space: nowrap; }
  .headline .word-top { display: block; font-size: 32px; }
  .headline .word-main { display: block; font-size: 37px; margin-top: 6px; }

  .rule { position: absolute; height: 1px; background: rgba(255,255,255,0.35); }

  .subline { position: absolute; font-size: 17px; line-height: 1.2; text-align: center; }

  .cta {
    position: absolute;
    display: flex; align-items: center; justify-content: center; gap: 6px;
    background: linear-gradient(180deg, var(--btn-top), var(--btn-bottom));
    border-radius: 5px;
    box-shadow: 0 2px 3px rgba(0,0,0,0.3);
    font-family: "Roboto Condensed", Arial, sans-serif; font-weight: 700;
    font-size: 18px; color: var(--btn-text); text-transform: uppercase;
    white-space: nowrap;
  }
  .cta svg { width: 18px; height: 18px; }

  .brand { position: absolute; text-align: center; }
  .brand-name { display: block; font-family: "Roboto", Arial, sans-serif; font-weight: 400; font-size: 42px; line-height: 1; color: var(--white); }
  .brand-tagline { display: block; font-size: 6.5px; letter-spacing: 0.2px; margin-top: 6px; text-transform: uppercase; white-space: nowrap; }

  /* Skyscraper */
  .banner--skyscraper { left: 174px; top: 136px; width: 200px; height: 750px; }
  .banner--skyscraper .headline { left: 0; width: 200px; top: 26px; }
  .banner--skyscraper .rule { left: 22px; width: 156px; top: 122px; }
  .banner--skyscraper .subline { left: 0; width: 200px; top: 138px; }
  .banner--skyscraper .cta { left: 20px; top: 610px; width: 160px; height: 42px; }
  .banner--skyscraper .brand { left: 0; width: 200px; top: 668px; }

  /* Large rectangle */
  .banner--rectangle-large { left: 494px; top: 136px; width: 425px; height: 353px; }
  .banner--rectangle-large .headline { left: 0; width: 190px; top: 26px; }
  .banner--rectangle-large .rule { left: 20px; width: 150px; top: 122px; }
  .banner--rectangle-large .subline { left: 0; width: 190px; top: 138px; }
  .banner--rectangle-large .cta { left: 13px; top: 214px; width: 160px; height: 41px; }
  .banner--rectangle-large .brand { left: 0; width: 190px; top: 276px; }

  /* Rectangle */
  .banner--rectangle { left: 512px; top: 564px; width: 388px; height: 323px; }
  .banner--rectangle .headline { left: 0; width: 172px; top: 22px; }
  .banner--rectangle .headline .word-top { font-size: 29px; }
  .banner--rectangle .headline .word-main { font-size: 33px; margin-top: 5px; }
  .banner--rectangle .rule { left: 18px; width: 136px; top: 110px; }
  .banner--rectangle .subline { left: 0; width: 172px; top: 126px; font-size: 15.5px; }
  .banner--rectangle .cta { left: 11px; top: 195px; width: 148px; height: 38px; font-size: 17px; }
  .banner--rectangle .brand { left: 0; width: 172px; top: 254px; }
  .banner--rectangle .brand-name { font-size: 38px; }

  /* Leaderboard */
  .banner--leaderboard { left: 174px; top: 939px; width: 910px; height: 113px; }
  .banner--leaderboard .brand { left: 8px; width: 148px; top: 28px; }
  .banner--leaderboard .brand-name { font-size: 40px; }
  .banner--leaderboard .divider { position: absolute; left: 160px; top: 14px; width: 1px; height: 85px; background: rgba(255,255,255,0.3); }
  .banner--leaderboard .headline { left: 170px; width: 196px; top: 16px; }
  .banner--leaderboard .headline .word-top { font-size: 31px; }
  .banner--leaderboard .headline .word-main { font-size: 37px; margin-top: 4px; }
  .banner--leaderboard .subline { left: 695px; width: 205px; top: 14px; font-size: 15.5px; }
  .banner--leaderboard .cta { left: 719px; top: 58px; width: 160px; height: 42px; }
</style>
</head>
<body>

<svg width="0" height="0" style="position:absolute">
  <defs>
    <linearGradient id="photo-tones" x1="0" y1="0" x2="1" y2="1">
      <stop offset="0" stop-color="#f3f1ee"/>
      <stop offset="0.55" stop-color="#dcd6cf"/>
      <stop offset="1" stop-color="#cdb8a3"/>
    </linearGradient>
    <symbol id="arrow-circle" viewBox="0 0 20 20">
      <circle cx="10" cy="10" r="9" fill="#2a1a00"/>
      <path d="M5 8.5h5V5.5l4.5 4.5-4.5 4.5v-3H5z" fill="#ffd21f"/>
    </symbol>
  </defs>
</svg>

<section class="banner banner--skyscraper">
  <svg class="photo-layer" viewBox="0 0 200 750" preserveAspectRatio="none">
    <path d="M0 246 Q100 200 200 232 L200 596 Q100 632 0 586 Z" fill="#8e0309"/>
    <path d="M0 254 Q100 210 200 240 L200 588 Q100 622 0 578 Z" fill="url(#photo-tones)" role="img" aria-label="Photo of a smiling young woman with a tape measure, holding a folder in a clothing studio"/>
  </svg>
  <h2 class="headline"><span class="word-top">Style</span><span class="word-main">Snacks</span></h2>
  <div class="rule"></div>
  <p class="subline">Short Courses<br>held in hotels in June<br>and July 2017</p>
  <a class="cta">Find out more <svg><use href="#arrow-circle"/></svg></a>
  <div class="brand"><span class="brand-name">QmV.rk</span><span class="brand-tagline">Institute of Style and Garment Care</span></div>
</section>

<section class="banner banner--rectangle-large">
  <svg class="photo-layer" viewBox="0 0 425 353" preserveAspectRatio="none">
    <path d="M232 0 Q138 176 220 353 L425 353 L425 0 Z" fill="#8e0309"/>
    <path d="M246 0 Q150 176 234 353 L425 353 L425 0 Z" fill="url(#photo-tones)" role="img" aria-label="Photo of a smiling young woman with a tape measure, holding a folder in a clothing studio"/>
  </svg>
  <h2 class="headline"><span class="word-top">Style</span><span class="word-main">Snacks</span></h2>
  <div class="rule"></div>
  <p class="subline">Short Courses<br>held in hotels in June<br>and July 2017</p>
  <a class="cta">Find out more <svg><use href="#arrow-circle"/></svg></a>
  <div class="brand"><span class="brand-name">QmV.rk</span><span class="brand-tagline">Institute of Style and Garment Care</span></div>
</section>

<section class="banner banner--rectangle">
  <svg class="photo-layer" viewBox="0 0 388 323" preserveAspectRatio="none">
    <path d="M208 0 Q128 162 200 323 L388 323 L388 0 Z" fill="#8e0309"/>
    <path d="M220 0 Q140 162 212 323 L388 323 L388 0 Z" fill="url(#photo-tones)" role="img" aria-label="Photo of a smiling young woman with a tape measure, holding a folder in a clothing studio"/>
  </svg>
  <h2 class="headline"><span class="word-top">Style</span><span class="word-main">Snacks</span></h2>
  <div class="rule"></div>
  <p class="subline">Short Courses<br>held in hotels in June<br>and July 2017</p>
  <a class="cta">Find out more <svg><use href="#arrow-circle"/></svg></a>
  <div class="brand"><span class="brand-name">QmV.rk</span><span class="brand-tagline">Institute of Style and Garment Care</span></div>
</section>

<section class="banner banner--leaderboard">
  <svg class="photo-layer" viewBox="0 0 910 113" preserveAspectRatio="none">
    <path d="M386 0 Q360 56 386 113 L688 113 Q712 56 688 0 Z" fill="#8e0309"/>
    <path d="M396 0 Q370 56 396 113 L678 113 Q702 56 678 0 Z" fill="url(#photo-tones)" role="img" aria-label="Photo of a smiling young woman with a tape measure, holding a folder in a clothing studio"/>
  </svg>
  <div class="brand"><span class="brand-name">QmV.rk</span><span class="brand-tagline">Institute of Style and Garment Care</span></div>
  <div class="divider"></div>
  <h2 class="headline"><span class="word-top">Style</span><span class="word-main">Snacks</span></h2>
  <p class="subline">Short Courses held in hotels<br>in June and July 2017</p>
  <a class="cta">Find out more <svg><use href="#arrow-circle"/></svg></a>
</section>

</body>
</html>
```